Mergers and Acquisitions Business Seeks Fresh Website Design

IMPORTANT: Please only design the Homepage, for the contest. If you win the contest, you will design the inner pages, as see in the attached document 'Travik 2025 website wireframes."
Design a new website for Travik at travik.global. Maintaining current Impact and Open Sans fonts, or using open-source alternatives from Google Fonts.
Enhance the design with a premium feel, impactful visuals, and dynamic content. We want the new design to focus on generating high-quality inquiries, strong calls to action, and consistent branding.
Industry/Entity Type
Mergers and Acquisitions
Number of Pages Required
5+ page
Font styles to use
Other font styles liked:
- See Website Brief file
Requirements
Must have
- Consistency in layout, colours, fonts and overall design
Should not have
- Very bright colours, hard to read fonts, unlicensed images and fonts

```html
<!DOCTYPE html>
<html lang="en">
<head>
<meta charset="utf-8">
<title>Travik – Homepage</title>
<link href="https://fonts.googleapis.com/css2?family=Oswald:wght@400;500;600;700&family=Open+Sans:wght@400;600;700&display=swap" rel="stylesheet">
<style>
:root{
  --plum:#52225e;
  --violet:#763f9a;
  --gold:#fbbf00;
  --grey:#666666;
  --white:#ffffff;
  --ink:#1d1d1f;
  --soft:#f5f5f6;
  --board:#e3e3e5;
  --display:'Oswald',sans-serif;
  --body:'Open Sans',sans-serif;
}
*{box-sizing:border-box;margin:0;padding:0}
html,body{width:1200px;height:4036px;overflow:hidden}
body{background:var(--board);font-family:var(--body);color:var(--ink);position:relative}
.page{position:absolute;left:262px;top:196px;width:675px;height:3780px;background:var(--white);overflow:hidden}
.wrap{width:495px;margin:0 auto}
.h2{font-family:var(--display);font-weight:600;text-transform:uppercase;text-align:center;font-size:20px;letter-spacing:.2px;color:var(--ink)}
.h2 .acc{color:var(--violet)}
.h2 .gold{color:var(--gold)}
/* header */
.site-header{height:39px;position:relative}
.brand{position:absolute;left:91px;top:9px;font-family:var(--display);font-weight:700;font-size:21px;color:var(--plum);letter-spacing:-.5px}
.utility{position:absolute;left:340px;top:6px;width:251px;height:14px;background:var(--soft);display:flex;justify-content:flex-end;align-items:center;gap:6px;font-size:5px}
.utility .phone{background:var(--gold);height:14px;padding:0 7px;display:flex;align-items:center;font-weight:700;color:var(--plum)}
.nav{position:absolute;left:346px;top:27px;display:flex;gap:34px;font-size:5px;color:var(--grey);text-transform:uppercase}
/* hero */
.hero{position:relative;margin:0 4px;height:312px;border-radius:3px;overflow:hidden}
.hero-photo{position:absolute;inset:0;background:radial-gradient(circle at 66% 40%,#9a9a9a 0%,#4a4a4a 26%,#1c1c1c 55%,#0d0d0d 100%)}
.hero-title{position:absolute;left:87px;top:155px;font-family:var(--display);font-weight:600;font-size:38px;line-height:40px;color:var(--white);text-transform:uppercase}
.hero-title .bar{color:var(--gold)}
.hero-select{display:inline-flex;align-items:center;justify-content:space-between;width:130px;height:28px;background:var(--white);border-radius:3px;vertical-align:middle;padding:0 8px;font-size:22px;color:var(--violet);margin-left:4px}
/* intro */
.intro{padding:38px 0 40px}
.intro p{width:395px;margin:10px auto 0;font-size:7.3px;line-height:11px;color:var(--grey)}
.intro p.lead{color:var(--ink);font-weight:600;margin-top:16px}
/* benefits */
.benefits{background:var(--soft);margin:0 4px;height:407px;padding-top:38px}
.benefits .h2{font-size:16px;line-height:21px;width:420px;margin:0 auto}
.grid{display:grid;grid-template-columns:repeat(4,1fr);gap:8px;width:495px;margin:27px auto 0}
.card{background:var(--white);height:118px;padding:18px 16px;border-radius:2px;box-shadow:0 1px 3px rgba(0,0,0,.06)}
.card.wide{grid-column:span 2}
.card.accent{background:linear-gradient(135deg,var(--plum),var(--violet));color:var(--white)}
.card svg{width:20px;height:20px;margin-bottom:14px}
.card h3{font-size:8.5px;font-weight:600;margin-bottom:5px}
.card p{font-size:6.4px;line-height:9px;color:var(--grey)}
.card.accent p{color:#e3d3ec}
/* video */
.video{position:relative;margin:12px 4px 0;height:326px;border-radius:3px;overflow:hidden;background:linear-gradient(90deg,#050505 0%,#111 45%,#3a3a3a 75%,#1a1a1a 100%)}
.play{position:absolute;left:84px;top:139px;width:48px;height:48px;border-radius:50%;background:var(--gold);border:3px solid #222;display:flex;align-items:center;justify-content:center}
/* sectors */
.sectors{padding-top:44px;text-align:center}
.tabs{display:flex;justify-content:center;gap:24px;margin-top:14px;font-size:7px;color:var(--grey)}
.tabs .on{color:var(--violet);font-weight:600}
.slider{position:relative;width:495px;height:197px;margin:18px auto 0}
.slide{position:absolute;inset:0;border-radius:3px;background:linear-gradient(180deg,#b9b9b9 0%,#6d6d6d 45%,#111 100%)}
.slide-copy{position:absolute;left:0;right:0;bottom:12px;color:var(--white);text-align:center}
.slide-copy h3{font-family:var(--display);font-size:18px;font-weight:600}
.slide-copy p{font-size:7px;margin-top:2px}
.arrow{position:absolute;top:88px;width:24px;height:24px;border-radius:50%;display:flex;align-items:center;justify-content:center;font-size:11px}
.arrow.prev{left:-12px;background:var(--white);color:var(--grey)}
.arrow.next{right:-12px;background:var(--plum);color:var(--white)}
/* contact cta */
.cta{padding-top:80px;text-align:center}
.cta p{width:340px;margin:12px auto 0;font-size:7px;line-height:11px;color:var(--grey)}
.cta-row{display:flex;justify-content:center;align-items:center;margin-top:22px}
.btn{display:inline-flex;align-items:center;justify-content:center;gap:6px;height:19px;padding:0 16px;font-size:6.5px;font-weight:600;border-radius:1px}
.btn.gold{background:var(--gold);color:var(--plum)}
.btn.plum{background:var(--plum);color:var(--white)}
.or{width:26px;height:26px;border-radius:50%;background:var(--white);box-shadow:0 1px 4px rgba(0,0,0,.15);display:flex;align-items:center;justify-content:center;font-size:7px;font-weight:700;margin:0 -3px;position:relative;z-index:1}
/* numbers */
.numbers{margin:50px 4px 0;height:239px;background:linear-gradient(135deg,var(--plum),var(--violet));color:var(--white);padding-top:40px}
.numbers .h2{color:var(--white);font-size:24px}
.stat{display:flex;align-items:center;justify-content:center;gap:36px;margin-top:20px}
.stat .ratio{font-family:var(--display);font-weight:500;font-size:118px;line-height:110px}
.stat p{font-size:21px;line-height:26px;width:210px}
/* case studies */
.cases{padding-top:48px}
.case-grid{display:grid;grid-template-columns:1fr 1fr;gap:9px;width:495px;margin:20px auto 0}
.case{position:relative;height:241px;border-radius:2px;overflow:hidden;background:linear-gradient(180deg,#d8d8d8 0%,#777 40%,#1a1a1a 100%);color:var(--white);text-align:center;display:flex;flex-direction:column;justify-content:flex-end;padding:0 30px 18px;font-size:11px;line-height:14px}
.case strong{display:block;margin:4px 0;font-size:12px}
.more{display:flex;justify-content:center;margin-top:25px}
/* insights */
.insights{background:var(--soft);margin:40px 4px 0;height:309px;padding-top:44px}
.post-grid{display:grid;grid-template-columns:repeat(4,1fr);gap:8px;width:495px;margin:20px auto 0}
.post{height:162px;border-radius:2px;background:linear-gradient(180deg,#8a8a8a 0%,#333 55%,#0d0d0d 100%);color:var(--white);display:flex;align-items:flex-end;justify-content:center;text-align:center;padding:0 8px 14px;font-size:7.3px;font-weight:600;line-height:10px}
.dots{display:flex;justify-content:center;gap:4px;margin-top:18px}
.dots i{width:4px;height:4px;border-radius:50%;background:#bbb}
.dots i.on{background:var(--violet)}
/* offices */
.offices{padding-top:52px}
.map{width:460px;height:227px;margin:26px auto 0;background:radial-gradient(ellipse at 30% 35%,#7a4a8c 0%,#c9d0d6 40%,#e1e6ea 70%,var(--white) 100%)}
.office-row{display:flex;justify-content:center;gap:150px;margin-top:42px;text-align:center}
.office h4{font-family:var(--display);font-size:10px;font-weight:600;margin-bottom:8px}
.office p{font-size:6.4px;line-height:10px;color:var(--grey)}
.office a{color:var(--plum);text-decoration:underline;font-size:6.4px}
/* footer */
.site-footer{position:absolute;left:4px;right:4px;bottom:4px;height:213px;background:linear-gradient(135deg,var(--plum),var(--violet));color:var(--white);padding:38px 84px 0}
.fcols{display:flex;gap:72px}
.fcol h4{font-family:var(--display);font-size:14px;font-weight:500;margin-bottom:10px}
.fcol ul{list-style:none;font-size:6px;line-height:16px;color:#e7dcee}
.fcol.services ul{columns:2;column-gap:22px}
.fcol.contact{margin-left:auto}
.fcol.contact .btn{display:flex;width:84px;margin-top:8px;height:18px;padding:0;font-size:5.5px}
.legal{position:absolute;left:84px;right:84px;bottom:16px;display:flex;justify-content:space-between;font-size:5px;color:#d8c8e2}
</style>
</head>
<body>
<div class="page">
  <header class="site-header">
    <div class="brand">travik</div>
    <div class="utility"><span>CONTACT US</span><span class="phone">01840 552 300</span></div>
    <nav class="nav"><span>Clients</span><span>Services</span><span>Case Studies</span><span>News</span><span>About</span></nav>
  </header>

  <section class="hero">
    <div class="hero-photo" role="img" aria-label="Monochrome photo of a hand holding a glass globe wrapped in a network of connected points"></div>
    <h1 class="hero-title"><span class="bar">I</span>DEAL<br>ORIGINATION<br>FOR <span class="hero-select">YOU? <svg width="8" height="5" viewBox="0 0 8 5"><path d="M1 1l3 3 3-3" stroke="#666" fill="none"/></svg></span></h1>
  </section>

  <section class="intro">
    <h2 class="h2">Exclusive deals, <span class="acc">reduced risk,</span> stronger leverage</h2>
    <p class="lead">We consistently deliver high-quality deals, bypassing the crowded open market. Imagine a pipeline filled with precise targets, aligned with your acquisition goals.</p>
    <p>Our approach minimises execution risk. We bring forward only well-matched prospects backed by transparent tracking and guidance. By specialising in off-market exclusivity, we enhance your negotiation leverage, reducing competition and securing favourable terms for both parties.</p>
    <p>We focus on quality over quantity, building high-trust seller relationships. Gain a competitive edge with our deep market knowledge and highly targeted outreach, expanding your market share. Travik enables you to acquire smarter, faster.</p>
  </section>

  <section class="benefits">
    <h2 class="h2">Travik empowers acquirers to <span class="acc">outpace competitors</span> by consistently delivering high-response, off-market deal flow, without adding headcount or overhead.</h2>
    <div class="grid">
      <div class="card"><svg viewBox="0 0 20 20" fill="none" stroke="#763f9a" stroke-width="1.2"><path d="M4 7h4V4h4v3h4v9H4z"/></svg><h3>Find the ideal fit</h3><p>Target businesses that match your exact criteria</p></div>
      <div class="card"><svg viewBox="0 0 20 20" fill="none" stroke="#763f9a" stroke-width="1.2"><circle cx="10" cy="10" r="3"/><path d="M10 2v4M10 14v4M2 10h4M14 10h4"/></svg><h3>More options</h3><p>Access businesses that aren't publicly listed</p></div>
      <div class="card wide accent"><svg viewBox="0 0 20 20" fill="none" stroke="#fff" stroke-width="1.2"><path d="M3 7h4l5-3v12l-5-3H3z"/><path d="M15 8l3 4M18 8l-3 4"/></svg><h3>No noise</h3><p>Avoid any unnecessary disruption from the advisors and brokers</p></div>
      <div class="card wide"><svg viewBox="0 0 20 20" fill="none" stroke="#763f9a" stroke-width="1.2"><path d="M2 10l5-4 3 2 3-2 5 4-8 5z"/></svg><h3>Higher-quality deals</h3><p>Engage directly with owners who prefer a discreet and low-profile sale</p></div>
      <div class="card"><svg viewBox="0 0 20 20" fill="none" stroke="#763f9a" stroke-width="1.2"><rect x="3" y="3" width="14" height="14"/><path d="M6 8h8M6 12h5"/></svg><h3>More control</h3><p>Move at your own pace, without broker pressure</p></div>
      <div class="card"><svg viewBox="0 0 20 20" fill="none" stroke="#763f9a" stroke-width="1.2"><circle cx="7" cy="7" r="3"/><path d="M2 17c0-4 10-4 10 0M13 11h5v6h-5z"/></svg><h3>Strong relationship</h3><p>Direct contact with business owners</p></div>
    </div>
  </section>

  <section class="video" role="img" aria-label="Dark close-up of a secure key fob with a lock symbol, video thumbnail">
    <div class="play"><svg width="14" height="14" viewBox="0 0 14 14"><path d="M3 1l10 6-10 6z" fill="#222"/></svg></div>
  </section>

  <section class="sectors">
    <h2 class="h2">We <span class="acc">work</span> for</h2>
    <div class="tabs"><span class="on">Private Equity</span><span>Trade Buyers</span><span>Sellers</span><span>MBI Candidates</span><span>Corporate Finance</span><span>Search Funds</span></div>
    <div class="slider">
      <div class="slide" role="img" aria-label="Monochrome photo of a business team meeting in a glass office"></div>
      <div class="slide-copy"><h3>PRIVATE EQUITY</h3><p>Expand your pipeline beyond traditional brokers and geographic boundaries.</p><p style="color:var(--gold);font-size:11px;margin-top:4px">›</p></div>
      <span class="arrow prev">‹</span><span class="arrow next">›</span>
    </div>
  </section>

  <section class="cta">
    <h2 class="h2">If you want <span class="acc">ideal flow,</span> let's talk</h2>
    <p>There is only so much you can tell from reviewing our website, the best way to explore is to have a short meeting with one of our team.</p>
    <div class="cta-row"><span class="btn gold">Contact Travik ›</span><span class="or">or</span><span class="btn plum">Book Appointment ›</span></div>
  </section>

  <section class="numbers">
    <h2 class="h2"><span class="gold">Travik</span> the numbers</h2>
    <div class="stat"><span class="ratio">1:5</span><p>For every 1 target approached, we analyse at least 5 companies!</p></div>
  </section>

  <section class="cases">
    <h2 class="h2">Recent <span class="acc">case</span> studies</h2>
    <div class="case-grid">
      <div class="case" role="img" aria-label="Monochrome photo of a handshake over a desk">Leading Labour Recruitment Company<strong>Acquired</strong>An Established Construction &amp; Recruitment Firm</div>
      <div class="case" role="img" aria-label="Monochrome photo of an office corridor">Fire Safety Focused Investment Group<strong>Acquired</strong>A bespoke Fire &amp; Security Solutions Business<span style="color:var(--gold);margin-top:4px">›</span></div>
      <div class="case" role="img" aria-label="Monochrome photo of an office with bookshelves">Fire Safety Focused Investment Group<strong>Acquired</strong>A bespoke Fire &amp; Security Solutions Business</div>
      <div class="case" role="img" aria-label="Monochrome photo of a handshake in a bright office">Leading Labour Recruitment Company<strong>Acquired</strong>An Established Construction &amp; Recruitment Firm</div>
    </div>
    <div class="more"><span class="btn gold">More Case Studies ›</span></div>
  </section>

  <section class="insights">
    <h2 class="h2"><span class="acc">M&amp;A insights</span> and latest trends</h2>
    <div class="post-grid">
      <div class="post" role="img" aria-label="Chess pieces on a board">Why the Off Market Is Key for the Motivated Buyer</div>
      <div class="post" role="img" aria-label="Business desk in low light">How to Finance Your Next Business Acquisition?</div>
      <div class="post" role="img" aria-label="Crowd of figures in a market">Is There Suitable Business for Sale Near Me?</div>
      <div class="post" role="img" aria-label="Hand signing a document">How to Finance Your Next Business Acquisition?</div>
    </div>
    <div class="dots"><i></i><i class="on"></i><i></i></div>
  </section>

  <section class="offices">
    <h2 class="h2">Regional and <span class="acc">cross-border</span> deal makers</h2>
    <div class="map" role="img" aria-label="World map with North America, UK, Europe, India and Australia highlighted in purple"></div>
    <div class="office-row">
      <div class="office"><h4>UK &amp; Europe Office</h4><p>Third Floor, Kestrel House<br>Wrenford<br>WF2 4LT</p><p style="margin-top:8px">Contact:</p><a>+44 (0) 1840 552 300</a></div>
      <div class="office"><h4>APAC Office</h4><p>12 Harbour Lane<br>Marrow Bay NSW 2010<br>Australia</p><p style="margin-top:8px">Contact:</p><a>+61 (0) 455 208 917</a></div>
    </div>
  </section>

  <footer class="site-footer">
    <div class="fcols">
      <div class="fcol"><h4>Clients</h4><ul><li>Private Equity</li><li>Trade Buyers</li><li>Management Buy In</li><li>Search Funds</li><li>Corporate Finance</li></ul></div>
      <div class="fcol services"><h4>Services</h4><ul><li>Deal Origination</li><li>Single Acquisitions</li><li>Buy and Build</li><li>Bolt-On Acquisitions</li><li>Cross Border / International</li><li>Acquisition Finance</li><li>Negotiation Support</li><li>Due Diligence</li></ul></div>
      <div class="fcol contact"><h4>Contact</h4><ul><li>+44 (0) 1840 552 300</li></ul><span class="btn gold">Contact Travik ›</span><span class="btn plum" style="background:#3e1848">Book Appointment ›</span></div>
    </div>
    <div class="legal"><span>(C) Travik All Rights Reserved</span><span>Policies | Terms of Use | Privacy Policy | Contact Us</span></div>
  </footer>
</div>
</body>
</html>
```